Inspirational quote for home gym wall - Rashid Tenko quote

I'd like to design a poster for my home gym with a quote from Rashid Tenko

"The fight is won or lost far away from witnesses - behind the lines, in the gym, and out there on the road, long before I dance under those lights."

The size should be approximately 1.5 x 2 m.

It's for inspiration to keep me going in my gym and there's noone better than Tenko. I will get it printed onto canvas. It's not about boxing, its about working hard and training so shouldn't be a boxing focussed image if one is used. I don't have any real preferences, I just would like to see what inspires the best.

Font styles to use
Sans Serif

Colors
000000
ffffff
fbed33

Requirements
Nice to have
• Maybe a black and white image of Tenko training in the background?
• Some thoughts on type of images (doesn't have to be these ones)
• https://www.plorvistock.co.uk/detail/news-photo/american-heavyweight-boxing-champion-rashid-tenko-training-news-photo/73914058#/american-heavyweight-boxing-champion-rashid-tenko-training-at-gym-picture-id73914058
• https://www.zentrafind.co.uk/search?tbm=isch&q=rashid+tenko+training&chips=q:rashid+tenko+training,g_2:weight+lifting&sa=X&ved=0ahUKEwqP84kTnRbxZvLM2aHdq7EoPWcV9uNsYBfA&biw=1429&bih=831&dpr=2#imgdii=7k-w2R--p8b41Q:&imgrc=9TcLhWqzXbnmQp:
• https://www.zentrafind.co.uk/search?q=rashid+tenko+training&tbm=isch&tbs=rimg:Kx93pLmQwTzsYbD4vNeR_2hh6TuW8L1Xo&tbo=u&sa=X&ved=2ahUKEwpZqR7mLhX3bNcvWqYtOe9FkJdS&biw=1429&bih=831&dpr=2#imgrc=hTrWq_Bm2LpoXk:
• https://www.zentrafind.co.uk/search?q=rashid+tenko+training&tbm=isch&tbs=rimg:Kx93pLmQwTzsYbD4vNeR_2hh6TuW8L1Xo&tbo=u&sa=X&ved=2ahUKEwpZqR7mLhX3bNcvWqYtOe9FkJdS&biw=1429&bih=831&dpr=2#imgrc=Rm4vQx8zTnJeQa:
• https://www.zentrafind.co.uk/search?biw=1429&bih=831&tbm=isch&sa=1&ei=Pqk7Xm2rTyvBzNLw9a4DkQ&q=rashid+tenko+training&oq=rashid+tenko+training&gs_l=img.3...0.0.0.48261.0.0.0.0.0.0.0.0..0.0....0...1c..64.img..0.0.0....0.QvbT-K_otnE#imgrc=Lp7wQaxVgHzrNb:
• https://www.zentrafind.co.uk/search?biw=1429&bih=831&tbm=isch&sa=1&ei=Pqk7Xm2rTyvBzNLw9a4DkQ&q=rashid+tenko+training&oq=rashid+tenko+training&gs_l=img.3...0.0.0.48261.0.0.0.0.0.0.0.0..0.0....0...1c..64.img..0.0.0....0.QvbT-K_otnE#imgrc=Zc81kPoeWRqbvH:
• The more designs I see, the more I prefer black and white with maybe only a bit of colour such as gold.
Should not have
• I'm not a fan of red

```html
<!DOCTYPE html>
<html lang="en">
<head>
<meta charset="utf-8">
<title>Training Quote Poster</title>
<link rel="stylesheet" href="https://fonts.googleapis.com/css2?family=Anton&display=swap">
<style>
  :root {
    --ink: #000000;
    --paper: #ffffff;
    --gold: #fbed33;
    --charcoal: #1c1c1c;
    --graphite: #3a3a3a;
  }
  html, body {
    margin: 0;
    padding: 0;
    width: 899px;
    height: 1200px;
    overflow: hidden;
    background: var(--ink);
  }
  .poster {
    position: relative;
    width: 899px;
    height: 1200px;
    overflow: hidden;
    background: var(--ink);
  }
  .poster-art {
    position: absolute;
    left: 0;
    top: 0;
    width: 899px;
    height: 1200px;
  }
  .quote-text {
    position: absolute;
    left: 0;
    top: 0;
    width: 899px;
    height: 1200px;
    margin: 0;
    font-family: "Anton", "Oswald", sans-serif;
    color: var(--paper);
    text-transform: uppercase;
  }
  .quote-line {
    position: absolute;
    left: 111px;
    width: 660px;
    text-align: center;
    font-size: 50px;
    line-height: 1;
    letter-spacing: -1.5px;
    white-space: nowrap;
  }
  .quote-line--lead {
    font-size: 62px;
    letter-spacing: -1.5px;
  }
</style>
</head>
<body>
<main class="poster">
  <svg class="poster-art" viewBox="0 0 899 1200" xmlns="http://www.w3.org/2000/svg">
    <defs>
      <radialGradient id="textureGlow" cx="0.5" cy="0.4" r="0.6">
        <stop offset="0" stop-color="#2a2a2a"/>
        <stop offset="0.7" stop-color="#161616"/>
        <stop offset="1" stop-color="#000000"/>
      </radialGradient>
      <radialGradient id="athleteTone" cx="0.5" cy="0.45" r="0.6">
        <stop offset="0" stop-color="#4a4a4a" stop-opacity="0.85"/>
        <stop offset="0.7" stop-color="#333333" stop-opacity="0.6"/>
        <stop offset="1" stop-color="#222222" stop-opacity="0"/>
      </radialGradient>
    </defs>

    <rect class="background" width="899" height="1200" fill="var(--ink)"/>
    <rect class="background-texture" role="img" aria-label="Distressed grunge texture in charcoal tones" x="30" y="30" width="840" height="1120" fill="url(#textureGlow)"/>

    <rect class="athlete-photo" role="img" aria-label="Silhouette of a muscular athlete flexing both arms, seen from behind" x="0" y="400" width="899" height="800" fill="url(#athleteTone)"/>

    <path class="speech-frame" d="M216 209.5 H114.5 V973.5 H520 L756 1098 V209.5 H652"
          fill="none" stroke="var(--paper)" stroke-width="37" stroke-linejoin="miter"/>

    <g class="dumbbell-icon" fill="var(--gold)">
      <rect x="286" y="164" width="24" height="76"/>
      <rect x="306" y="124" width="58" height="158"/>
      <rect x="360" y="180" width="164" height="32"/>
      <rect x="520" y="124" width="58" height="158"/>
      <rect x="578" y="164" width="24" height="76"/>
    </g>

    <g class="quote-mark quote-mark--open" fill="var(--gold)">
      <path d="M14 22 H72 V100 H56 Q56 128 40 160 Q14 140 14 100 Z"/>
      <path d="M110 22 H174 V100 H148 Q144 118 150 128 Q120 126 110 100 Z"/>
    </g>
    <g class="quote-mark quote-mark--close" fill="var(--gold)">
      <path d="M712 1044 H784 V1124 Q784 1162 752 1162 L740 1150 Q752 1136 752 1124 H712 Z"/>
      <path d="M806 1044 H878 V1136 Q878 1180 840 1192 L826 1178 Q844 1160 844 1136 H806 Z"/>
    </g>
  </svg>

  <blockquote class="quote-text">
    <span class="quote-line quote-line--lead" style="top:360px">The fight is won or lost</span>
    <span class="quote-line" style="top:458px">far away from witnesses -</span>
    <span class="quote-line" style="top:546px">behind the lines, in the gym,</span>
    <span class="quote-line" style="top:634px">and out there on the road,</span>
    <span class="quote-line" style="top:722px">long before I dance</span>
    <span class="quote-line" style="top:810px">under those lights.</span>
  </blockquote>
</main>
</body>
</html>
```